Design Briefpapier
Zielgruppe
Veranstaltungstechnik
Aufgabenstellung
Wir möchten unser Layout (Briefkopf, Header, Footer) neu gestalten lassen. Es existiert bereits ein Logo, das leicht verändert im Header erscheinen soll! WICHTIG: Das Logo soll schwarz hinterlegt werden auf dem Briefpapier, damit das eigentliche Design (orange auf schwarz) auch zur Geltung kommt.
Marke für hochwertige Trauerartikel benötigt Briefpapier Marke für hochwertige Trauerartikel benötigt Briefpapier"
Wir benötigen Briefpapier: Anschreiben, Rechnngsformular in Farbe und in schwarz weiß. Dazu Visitenkarten und ein gleicherscheinenden E-Mail Absender. Das Design sollte so klar wir möglich sein. Der Druck erfolgt auf recyceltem Papier.
Briefpapierbogen-/Visitenkarten-Design für KFZ-Unternehmen Briefpapierbogen-/Visitenkarten-Design für KFZ-Unternehmen"
Wir benötigen ein Briefpapierbogen sowie ein Visitenkarten Design! Folgende Angaben müssen auf dem Briefpapier sein: - Logo (siehe Anhang) - Anschrift (KW Solutions UG (haftungsbeschränkt), Tannweg 7, 75412 Borlingen - Wasserzeichen - GF (Jürgen Talkeni) - Bankverbindung ( IBAN DE42 8157 2290..
Briefpapier für Seehafenspedition im Bereich Zollabfertigung Briefpapier für Seehafenspedition im Bereich Zollabfertigung"
Wir bitten um ein Design für unser Briefpapier. Wir suchen ein hochwertiges Design, das die Werte Vertrauen, Exklusivität und Innovation ausstrahlt. Es soll edel aussehen. Bitte für Telefon, Mail etc. Icons benutzen, damit es für jedermann verständlich ist, unabhängig von der Sprach..
Geschäftspapiere für medizinische Schutzausrüstung Geschäftspapiere für medizinische Schutzausrüstung"
Es sollte clean sein, Farben wie , Weiß, blau, grün, wären von Vorteil. Habe keine besondere Vorstellungen lasse mich gerne überraschen. Siehe .. www.vaskoru.de
Geschäftspapiere für Rechtsanwaltskanzlei Geschäftspapiere für Rechtsanwaltskanzlei"
Bitte inklusive Logo (sollte Recht, Digital/Apps, Medizin illustrieren) - habe das Preisgeld vor diesem Hintergrund erhöht. ------------------------- Die Kanzlei arbeitet an der Schnittstelle von (Medizin-)Recht und Digital. Von daher wären wären Symbole/Gestaltung aus Bereich Medizin, Recht..

```html
<!DOCTYPE html>
<html lang="de">
<head>
<meta charset="utf-8">
<title>Briefbogen klangwerk brandt</title>
<link rel="stylesheet" href="https://fonts.googleapis.com/css2?family=Jost:wght@400;500;600;700&display=swap">
<style>
  :root {
    --orange: #f07d00;
    --black: #000000;
    --ink: #111111;
    --paper: #ffffff;
    --side-top: #ffffff;
    --side-bottom: #ececec;
    --signature: #2b3390;
  }
  * { box-sizing: border-box; margin: 0; padding: 0; }
  html, body { width: 873px; height: 1200px; overflow: hidden; background: var(--paper); }
  body { font-family: "Jost", sans-serif; color: var(--ink); }
  .sheet { position: relative; width: 873px; height: 1200px; overflow: hidden; background: var(--paper); }

  .top-band { position: absolute; left: 0; top: 0; width: 873px; height: 36px; background: var(--orange); }
  .header-bar {
    position: absolute; left: 72px; top: 36px; width: 801px; height: 76px;
    background: var(--black); border-radius: 38px 0 0 38px;
    display: flex; align-items: center; padding-left: 26px; gap: 12px;
  }
  .brand-dot { width: 34px; height: 34px; border-radius: 50%; background: var(--orange); }
  .brand-name { color: #fff; font-size: 34px; font-weight: 500; letter-spacing: 0.2px; line-height: 1; }

  .sidebar {
    position: absolute; left: 671px; top: 112px; width: 202px; height: 1088px;
    background: linear-gradient(to bottom, var(--side-top) 0%, var(--side-top) 20%, var(--side-bottom) 100%);
  }

  .sender-line { position: absolute; left: 84px; top: 192px; font-size: 8.5px; letter-spacing: 0.1px; }
  .recipient { position: absolute; left: 84px; top: 276px; font-size: 13.5px; line-height: 17px; letter-spacing: 0.9px; }
  .recipient .company { font-weight: 600; }
  .recipient .city { margin-top: 17px; }

  .contact { position: absolute; left: 687px; top: 192px; font-size: 8.5px; line-height: 11px; }
  .contact .company { color: var(--orange); font-weight: 600; }
  .contact .gap { margin-top: 12px; }

  .subject { position: absolute; left: 84px; top: 466px; font-size: 15px; font-weight: 600; letter-spacing: 1.1px; }
  .date { position: absolute; left: 687px; top: 467px; font-size: 13.5px; letter-spacing: 0.9px; }

  .letter-body { position: absolute; left: 84px; top: 525px; width: 570px; font-size: 13.3px; line-height: 17.3px; letter-spacing: 0.75px; }
  .letter-body p { margin-bottom: 17.3px; }
  .letter-body .salutation { margin-bottom: 34px; }
  .closing { position: absolute; left: 84px; top: 902px; font-size: 13.5px; letter-spacing: 0.8px; }
  .signature { position: absolute; left: 76px; top: 935px; width: 230px; height: 50px; background: linear-gradient(90deg, rgba(43,51,144,0.16), rgba(43,51,144,0.04)); border-radius: 4px; }
  .signer { position: absolute; left: 84px; top: 989px; font-size: 13px; letter-spacing: 0.9px; line-height: 16px; }
  .signer .role { font-style: italic; font-size: 11.5px; }

  .legal { position: absolute; left: 687px; top: 934px; font-size: 7.3px; line-height: 9.6px; }
  .legal .block { margin-bottom: 9.6px; }
  .legal-rule { position: absolute; left: 671px; width: 16px; height: 1px; background: var(--ink); }

  .footer-rule { position: absolute; left: 0; top: 1145px; width: 671px; height: 4px; background: var(--orange); }
  .footer-bar {
    position: absolute; left: 0; top: 1149px; width: 671px; height: 51px; background: var(--black);
    color: #fff; font-size: 13px; font-weight: 600; letter-spacing: 0.3px;
    display: flex; align-items: center; padding-left: 94px;
  }
  .footer-url { position: absolute; left: 687px; top: 1168px; color: var(--orange); font-size: 11.5px; font-weight: 600; }
</style>
</head>
<body>
<div class="sheet">
  <div class="top-band"></div>
  <div class="header-bar">
    <span class="brand-dot"></span>
    <span class="brand-name">klangwerk brandt</span>
  </div>
  <div class="sidebar"></div>

  <div class="sender-line">klangwerk brandt GmbH &amp; Co. KG &nbsp;·&nbsp; Lindenhofstr. 14 &nbsp;·&nbsp; 10963 Berlin</div>

  <address class="recipient" style="font-style:normal">
    <div class="company">Firma Mustermeyer</div>
    <div>Herr Max Mustermeier</div>
    <div>Musterstraße 123</div>
    <div class="city">12345 Musterstadt</div>
  </address>

  <address class="contact" style="font-style:normal">
    <div class="company">klangwerk brandt GmbH &amp; Co. KG</div>
    <div>Lindenhofstr. 14 &nbsp;·&nbsp; 10963 Berlin</div>
    <div class="gap">Tel. 030 555 018 42</div>
    <div>Fax. 030 555 018 43</div>
    <div class="gap">info@klangwerk-brandt.de</div>
  </address>

  <div class="subject">Hier steht die Betreffzeile</div>
  <div class="date">Berlin, 01.10.2014</div>

  <div class="letter-body">
    <p class="salutation">Sehr geehrter Herr Mustermann,</p>
    <p>Interdum volgus rectum videt, est ubi peccat. Si veteres ita miratur laudatque poetas, ut nihil anteferat, nihil illis comparet, errat. Si quaedam nimis antique, si peraque dure dicere credit eos, ignave multa fatetur, et sapit et mecum facit et Iova iudicat aequo.</p>
    <p>Non equidem insector delendave carmina Livi esse reor, memini quae plagosum mihi parvo Orbilium dictare; sed emendata videri pulchraque et exactis minimum distantia miror. Inter quae verbum emicuit si forte decorum, et si versus paulo concinnior unus et alter, venditque poema.</p>
    <p>Indignor quicquam reprehendi, non quia crasse compositum illepedeve putetur, sed quia nuper, nec veniam antiquis, sed honorem et praemia posci. Recte necne crocum floresque perambulet Attae fabula si dubitem, clament periisse pudorem cuncti paene patres, ea cum reprehendere coner, quae gravis Aesopus, quae doctus Roscius egit; vel quia nil rectum, nisi quod placuit sibi, ducunt, vel quia turpe putant parere mino-ribus, et quae imberbes senes.</p>
  </div>

  <div class="closing">Mit freundlichen Grüßen,</div>
  <div class="signature" role="img" aria-label="Handschriftliche Unterschrift des Geschäftsführers"></div>
  <div class="signer">
    <div>Tobias Rahnfeld</div>
    <div class="role">Geschäftsführer</div>
  </div>

  <div class="legal">
    <div class="block">Bankverbindung: Spreeland Bank<br>Konto: 0471120933 &nbsp;·&nbsp; BLZ: 100 512 77</div>
    <div class="block">IBAN: DE18 1005 1277 0471 1209 33<br>BIC / SWIFT: SPRL DE BB 210</div>
    <div class="block" style="margin-top:13px">Sitz der Gesellschaft: Berlin<br>Amtsgericht Berlin &nbsp;·&nbsp; HRA 12345</div>
    <div class="block">Geschäftsführer:<br>Tobias Rahnfeld, Jonas Kellerbach<br>USt-ID: DE318642097</div>
    <div class="block" style="margin-top:13px">Persönlich haftende Gesellschafterin:<br>klangwerk brandt Verwaltungs-GmbH</div>
    <div class="block">Geschäftsführer:<br>Tobias Rahnfeld, Jonas Kellerbach<br>Amtsgericht Berlin &nbsp;·&nbsp; HRB 12345</div>
  </div>
  <div class="legal-rule" style="top:995px"></div>
  <div class="legal-rule" style="top:1026px"></div>

  <div class="footer-rule"></div>
  <div class="footer-bar">The only goog system is a Soundsystem &nbsp;—&nbsp; Tuned by Klangwerk Brandt</div>
  <div class="footer-url">www.klangwerk-brandt.de</div>
</div>
</body>
</html>
```